Eye Doctor Needs Updated Business Card

We need a standard US business card designed for an optometrist's practice. Our practice name is Halvorn Vision Center and attached you'll find our logos. We are located in a smaller community, we are a trusted source for eye care and designer eyewear. We have 2 different version of our logos, so both versions are attached. Our slogan is "Small Town Values, World Class Care". I'd like to see designs with one of our logos on the front with our contact info, and have the slogan on the back by itself. Final design should be professional looking, include the colors of our logo or colors that compliment the logo. We want it to look appropriate for a healthcare practice but also up-to-date, eye-catching, to have the normal contact info like address, phone #, email, but also possibly room for additional contact info such as facebook.
Updates

I just uploaded .eps files to use instead of the jpeg. Hope that helps!

So many great designs! We tending to like the darker blues that are used in our logo as the main blue color for the business cards. We also really like the use of a water-mark type appearance on either the front and/or back, or the embossed look as well looks nice. Thank you all for such great designs!

We're preferring the designs where white and the darker blue used in our logo are the primary colors on the front, but with a little green used as well. Again though, thanks for all the impressive designs so far!

Industry/Entity Type

Healthcare

```html
<!DOCTYPE html>
<html lang="en">
<head>
<meta charset="utf-8">
<title>Halvorn Vision Center – Business Card</title>
<link rel="stylesheet" href="https://fonts.googleapis.com/css2?family=Didact+Gothic&display=swap">
<style>
  :root {
    --backdrop: #5d6675;
    --card: #f3f4f5;
    --navy: #1f2a5a;
    --ink: #55585e;
    --blue-deep: #1b3db3;
    --blue-mid: #2f6fe0;
    --blue-light: #8cc6ee;
    --blue-pale: #d7e8f6;
    --green: #4fa23a;
  }
  html, body {
    margin: 0;
    width: 1200px;
    height: 1000px;
    overflow: hidden;
    background: var(--backdrop);
    font-family: "Didact Gothic", "Century Gothic", sans-serif;
  }
  .canvas {
    position: relative;
    width: 1200px;
    height: 1000px;
  }
  .card {
    position: absolute;
    left: 250px;
    width: 700px;
    height: 400px;
    background: var(--card);
    overflow: hidden;
    box-shadow: 0 6px 18px rgba(0,0,0,.25);
  }
  .card--back { top: 60px; }
  .card--front { top: 540px; }
  .card__waves {
    position: absolute;
    inset: 0;
    width: 100%;
    height: 100%;
  }
  .brand {
    position: absolute;
    display: flex;
    align-items: center;
    gap: 14px;
    color: var(--navy);
    letter-spacing: .04em;
  }
  .brand__dot {
    border-radius: 50%;
    background: var(--green);
    flex: none;
  }
  .card--back .brand {
    top: 70px;
    left: 0;
    right: 0;
    justify-content: center;
    font-size: 30px;
  }
  .card--back .brand__dot { width: 22px; height: 22px; }
  .tagline {
    position: absolute;
    top: 130px;
    left: 0;
    right: 0;
    text-align: center;
    font-size: 30px;
    color: var(--ink);
    letter-spacing: .03em;
  }
  .card--front .brand {
    top: 150px;
    left: 50px;
    flex-direction: column;
    align-items: flex-start;
    gap: 12px;
    font-size: 30px;
  }
  .card--front .brand__dot { width: 46px; height: 46px; margin-left: 60px; }
  .contact {
    position: absolute;
    top: 60px;
    left: 390px;
    color: var(--ink);
  }
  .contact__name {
    font-size: 28px;
    margin: 0 0 12px;
    font-weight: 400;
  }
  .contact__line {
    margin: 0;
    font-size: 16px;
    line-height: 1.6;
  }
</style>
</head>
<body>
<main class="canvas">

  <section class="card card--back" aria-label="Business card back">
    <svg class="card__waves" viewBox="0 0 700 400" aria-hidden="true">
      <defs>
        <radialGradient id="halftone-back" cx="0.85" cy="0.1" r="0.6">
          <stop offset="0" stop-color="var(--blue-light)" stop-opacity=".55"/>
          <stop offset="1" stop-color="var(--blue-light)" stop-opacity="0"/>
        </radialGradient>
      </defs>
      <rect x="380" y="0" width="320" height="260" fill="url(#halftone-back)" role="img" aria-label="Soft halftone dot texture"/>
      <path d="M0 260 C 220 200, 480 200, 700 150 L700 175 C 480 225, 220 230, 0 290 Z" fill="var(--blue-pale)"/>
      <path d="M0 400 C 180 330, 430 290, 700 170 L700 215 C 460 320, 230 360, 90 400 Z" fill="var(--blue-light)"/>
      <path d="M0 380 C 190 300, 440 260, 700 140 L700 165 C 450 290, 220 330, 0 400 Z" fill="var(--blue-deep)"/>
      <path d="M600 0 C 640 80, 680 140, 700 160 L700 110 C 680 80, 650 40, 640 0 Z" fill="var(--blue-mid)"/>
    </svg>
    <div class="brand">
      <span class="brand__dot"></span>
      <span class="brand__name">Halvorn Vision Center</span>
    </div>
    <p class="tagline">Your Sample Text Logo</p>
  </section>

  <section class="card card--front" aria-label="Business card front">
    <svg class="card__waves" viewBox="0 0 700 400" aria-hidden="true">
      <defs>
        <radialGradient id="halftone-front" cx="0.85" cy="0.3" r="0.6">
          <stop offset="0" stop-color="var(--blue-light)" stop-opacity=".6"/>
          <stop offset="1" stop-color="var(--blue-light)" stop-opacity="0"/>
        </radialGradient>
      </defs>
      <rect x="420" y="0" width="280" height="300" fill="url(#halftone-front)" role="img" aria-label="Soft halftone dot texture"/>
      <path d="M0 290 C 220 250, 470 250, 700 230 L700 250 C 470 270, 220 280, 0 320 Z" fill="var(--blue-pale)"/>
      <path d="M70 400 C 260 330, 500 290, 700 180 L700 230 C 520 320, 320 370, 200 400 Z" fill="var(--blue-light)"/>
      <path d="M0 400 C 220 320, 470 270, 700 160 L700 185 C 480 300, 250 360, 60 400 Z" fill="var(--blue-deep)"/>
      <path d="M610 0 C 650 80, 690 150, 700 170 L700 110 C 690 80, 660 30, 650 0 Z" fill="var(--blue-mid)"/>
    </svg>
    <div class="brand">
      <span class="brand__dot"></span>
      <span class="brand__name">Halvorn Vision Center</span>
    </div>
    <div class="contact">
      <h2 class="contact__name">Employee Name</h2>
      <p class="contact__line">Mobile 0000 000 000</p>
      <p class="contact__line">email: yourmail@mail.com</p>
      <p class="contact__line">sitename1.com.usa</p>
    </div>
  </section>

</main>
</body>
</html>
```